Business card por a urban DJ, up scale audience target

Need a sober design, modern, conservative colors but i can consider some options, y play rnb, hip hop, EDM and top40.

Business card for contact and personal info, double sided, use logo attrached please; im 42 so i need a card acording to my age an target audience.

Target Market(s)

Adult people, up scale audience

Industry/Entity Type

Music Download

Contact Information for Business Card

Cel (318) 5024471963 www.kelvarodun.com

Requirements
Must have
• open mind
Nice to have
• open mind
Should not have
• DJ

```html
<!DOCTYPE html>
<html lang="en">
<head>
<meta charset="utf-8">
<title>Kelvar Business Card</title>
<link href="https://fonts.googleapis.com/css2?family=Montserrat:wght@600;800&display=swap" rel="stylesheet">
<style>
  :root {
    --backdrop: #e6e6e6;
    --card-dark: #3b3b3b;
    --card-light: #f4f4f4;
    --edge-grey: #cfcfcf;
    --ink-dark: #2f2f2f;
    --ink-light: #ffffff;
    --name-silver: #d9d9d9;
  }
  * { margin: 0; padding: 0; box-sizing: border-box; }
  html, body {
    width: 1200px;
    height: 800px;
    overflow: hidden;
    background: var(--backdrop);
    font-family: "Montserrat", sans-serif;
  }
  .sheet {
    position: relative;
    width: 1200px;
    height: 800px;
    display: flex;
    align-items: center;
    justify-content: center;
    gap: 40px;
  }
  .card {
    position: relative;
    width: 520px;
    height: 297px;
    background: var(--card-dark);
    overflow: hidden;
    box-shadow: 0 6px 18px rgba(0,0,0,0.18);
  }
  .card-front .wave {
    position: absolute;
    inset: 0;
    width: 100%;
    height: 100%;
  }
  .contact-list {
    position: absolute;
    left: 32px;
    top: 74px;
    list-style: none;
    color: var(--ink-dark);
    font-weight: 600;
    font-size: 15px;
    letter-spacing: 0.05em;
  }
  .contact-list li {
    display: flex;
    align-items: center;
    gap: 9px;
    margin-bottom: 20px;
  }
  .contact-list svg { width: 14px; height: 16px; flex: none; }
  .brand {
    position: absolute;
    right: 30px;
    top: 104px;
    color: var(--ink-light);
  }
  .brand-name {
    font-weight: 800;
    font-size: 42px;
    letter-spacing: 0.04em;
    line-height: 1;
  }
  .brand-genres {
    margin-top: 8px;
    font-weight: 800;
    font-size: 11px;
    letter-spacing: 0.3em;
  }
  .card-back {
    display: flex;
    align-items: center;
    justify-content: center;
  }
  .card-back .brand-name {
    color: var(--name-silver);
    font-size: 64px;
  }
</style>
</head>
<body>
  <main class="sheet">
    <section class="card card-front" aria-label="Card front">
      <svg class="wave" viewBox="0 0 520 297" preserveAspectRatio="none" aria-hidden="true">
        <path d="M0,14 C80,4 160,0 212,24 C262,50 272,168 322,228 C362,272 460,284 520,286 L520,297 L0,297 Z" fill="var(--edge-grey)"/>
        <path d="M0,20 C80,10 156,6 204,30 C252,56 262,172 312,234 C352,280 456,290 520,292 L520,297 L0,297 Z" fill="var(--card-light)"/>
      </svg>
      <ul class="contact-list">
        <li>
          <svg viewBox="0 0 14 16" aria-hidden="true"><rect x="3" y="1" width="8" height="14" rx="1.5" fill="none" stroke="currentColor" stroke-width="1.6"/><rect x="6" y="12" width="2" height="1.4" fill="currentColor"/></svg>
          (318) 502.447.1963
        </li>
        <li>
          <svg viewBox="0 0 16 16" aria-hidden="true"><circle cx="8" cy="8" r="6.5" fill="none" stroke="currentColor" stroke-width="1.6"/><ellipse cx="8" cy="8" rx="2.8" ry="6.5" fill="none" stroke="currentColor" stroke-width="1.2"/><line x1="1.5" y1="8" x2="14.5" y2="8" stroke="currentColor" stroke-width="1.2"/></svg>
          www.kelvarodun.com
        </li>
      </ul>
      <div class="brand">
        <div class="brand-name">KELVAR</div>
        <div class="brand-genres">RNB HIPHOP EDM</div>
      </div>
    </section>
    <section class="card card-back" aria-label="Card back">
      <div class="brand-name">KELVAR</div>
    </section>
  </main>
</body>
</html>
```